Specialist Technical Theatre service for schools

The task is to design a brochure (A5, 4 pages) for mailing to secondary/high school heads and drama departments to sell them our services as Technical Theatre and Drama professionals who can help them to offer elements of a curriculum that they do not currently offer as well as raise the technical standards of their school productions.
Please find a document attached which outlines the content for the brochure. Please read the document first so that you understand our aims. The text highlighted in yellow takes priority - the text highlighted in blue could be used if there is space.
Photos which may be used available on https://www.snapvault.example/photos/ben_torvik/ (please do not use watermarked morrow pictures).
Logo is attached (two variants) - one of which should appear somewhere on the design. Website address is www.bentorvik.co.uk and email is info@bentorvik.co.uk
Target Market(s)
Theatre and Drama teachers in Secondary/High schools
Headteachers of Secondary/High Schools
Industry/Entity Type
Education
Look and feel

```html
<!DOCTYPE html>
<html lang="en">
<head>
<meta charset="utf-8">
<title>School Technical Theatre brochure</title>
<link rel="stylesheet" href="https://fonts.googleapis.com/css2?family=Cinzel:wght@600&family=Crimson+Text:wght@400;600&family=Lato:wght@300;400&display=swap">
<style>
:root{
  --navy:#2b3462;
  --navy-light:#4b5588;
  --gold:#c98a12;
  --gold-light:#e6ad3c;
  --paper:#f1f1f2;
  --paper-dark:#dcdcde;
  --ink:#2a2a33;
  --backdrop:#e8e3da;
}
*{box-sizing:border-box;margin:0;padding:0}
html,body{width:1200px;height:1121px;overflow:hidden}
body{background:var(--backdrop);position:relative;font-family:"Lato",sans-serif;color:var(--ink)}
.spread{position:absolute;width:698px;height:490px;overflow:hidden;box-shadow:0 6px 18px rgba(0,0,0,.25)}
.spread-outside{left:46px;top:54px}
.spread-inside{left:461px;top:586px;background:linear-gradient(90deg,#fff 0%,var(--paper) 48%,var(--paper-dark) 50%,#fff 51%,var(--paper) 100%)}
.page{position:absolute;top:0;width:349px;height:490px;overflow:hidden}
.page-left{left:0}
.page-right{left:349px}
.spread-art{position:absolute;inset:0}

/* back cover */
.back-cover{background:radial-gradient(ellipse at 50% 30%,#fafafa,#dedee0)}
.contact{position:absolute;top:26px;left:0;width:100%;text-align:center}
.contact-title{font-family:"Crimson Text",serif;font-weight:600;font-size:18px;color:var(--navy);margin-bottom:4px}
.contact-line{font-size:10px;color:var(--ink);line-height:16px;display:flex;align-items:center;justify-content:center;gap:4px}
.contact-line.phone{font-size:13px}
.contact-line svg{width:9px;height:9px}
.brand{display:flex;align-items:center;justify-content:center;gap:6px}
.brand-dot{width:12px;height:12px;border-radius:50%;background:var(--gold)}
.brand-name{font-family:"Crimson Text",serif;font-weight:600}
.back-brand{position:absolute;top:180px;left:0;width:100%;text-align:center}
.back-brand .brand-name{font-size:17px;color:var(--navy)}
.back-brand .tagline{font-family:"Crimson Text",serif;font-size:5.5px;letter-spacing:.4px;color:var(--ink);margin-top:3px;line-height:7px}
.badges{position:absolute;top:218px;left:72px;display:flex;gap:18px;align-items:center}
.badge{width:30px;height:22px;background:#cfcfd4;border-radius:3px}
.badge.round{width:24px;height:24px;border-radius:50%;background:#e8cf3f}

/* front cover */
.front-brand{position:absolute;top:34px;left:0;width:100%}
.front-brand .brand-name{font-size:22px;color:var(--gold-light)}
.front-tagline{position:absolute;top:93px;left:0;width:100%;text-align:center;font-family:"Crimson Text",serif;font-size:12.5px;line-height:14.5px;color:#fff;letter-spacing:.3px}
.front-title{position:absolute;top:430px;left:0;width:100%;text-align:center;font-family:"Cinzel",serif;font-weight:600;font-size:19px;color:var(--navy);letter-spacing:.2px}
.front-subtitle{position:absolute;top:454px;left:0;width:100%;text-align:center;font-family:"Crimson Text",serif;font-size:18px;color:#1b1b22}

/* inside */
.copy{position:absolute;font-size:7.2px;line-height:9.1px;color:#333}
.copy-left{left:16px;top:20px;width:318px}
.copy-right{left:18px;top:20px;width:318px}
.copy p{margin-bottom:4px;text-align:justify}
.lead{font-size:7.6px;line-height:9.6px}
.callout{position:relative;font-family:"Crimson Text",serif;font-size:7.8px;line-height:9px;color:#1e1e26;margin:6px 0 4px;padding-left:0}
.callout::before{content:"";position:absolute;left:-16px;top:0;width:11px;height:100%;background:var(--gold)}
.copy-right .callout::before{left:-18px}
.source{font-family:"Crimson Text",serif;font-size:5.6px;color:#555;margin:-2px 0 5px}
.list{list-style:none;margin:0 0 4px 10px}
.list li{position:relative;padding-left:10px;margin-bottom:5.2px;line-height:8.4px}
.list li::before{content:"";position:absolute;left:0;top:2.5px;width:3.5px;height:3.5px;border-radius:50%;background:var(--gold)}
.list.narrow li{max-width:222px}
.copy-right .list li{margin-bottom:3px}
.quotes{list-style:none;margin-left:0}
.quotes li{position:relative;padding:0 4px 0 11px;margin-bottom:8px;text-align:justify;line-height:8.8px}
.quotes li::before{content:"\201C";position:absolute;left:0;top:-2px;font-size:11px;font-family:"Crimson Text",serif;font-weight:600}
.quotes li::after{content:"\201D";font-size:11px;font-family:"Crimson Text",serif;font-weight:600;margin-left:2px;line-height:0;position:relative;top:4px}
.note{font-size:5.4px;line-height:6.5px;margin-top:-2px}
.strong{font-weight:400;color:#111}
.badge-photo{position:absolute;left:235px;top:122px;width:96px;height:96px}
.desk-photo{position:absolute;left:0;top:326px;width:349px;height:164px}
</style>
</head>
<body>

<section class="spread spread-outside" aria-label="Brochure outside spread">
  <div class="page page-left back-cover">
    <div class="contact">
      <h2 class="contact-title">Contact Us</h2>
      <p class="contact-line phone"><svg viewBox="0 0 10 10"><path d="M2 0.5 L4 2.5 L3 4 Q4.5 6 6 7 L7.5 6 L9.5 8 L8 9.5 Q3 9 0.5 2 Z" fill="var(--gold)"/></svg>+44 7700 900412</p>
      <p class="contact-line"><svg viewBox="0 0 10 10"><rect x="0.5" y="2" width="9" height="6.5" fill="var(--gold)"/><path d="M0.5 2 L5 6 L9.5 2" stroke="#fff" fill="none" stroke-width="0.8"/></svg>info@bentorvik.co.uk</p>
      <p class="contact-line"><svg viewBox="0 0 10 10"><circle cx="5" cy="5" r="4.5" fill="var(--gold)"/><path d="M0.5 5 H9.5 M5 0.5 V9.5" stroke="#fff" stroke-width="0.6"/></svg>www.bentorvik.co.uk</p>
    </div>
    <div class="back-brand">
      <div class="brand"><span class="brand-dot"></span><span class="brand-name">Ben Torvik</span></div>
      <p class="tagline">STAGE AND<br>PRODUCTION MANAGEMENT</p>
    </div>
    <div class="badges">
      <span class="badge"></span><span class="badge"></span><span class="badge round"></span><span class="badge"></span>
    </div>
  </div>

  <div class="page page-right front-cover"></div>

  <svg class="spread-art" viewBox="0 0 698 490" aria-hidden="false">
    <defs>
      <linearGradient id="navyFade" x1="0" y1="0" x2="0" y2="1">
        <stop offset="0" stop-color="var(--navy)"/>
        <stop offset="0.75" stop-color="var(--navy-light)"/>
        <stop offset="1" stop-color="#8a90b0"/>
      </linearGradient>
      <linearGradient id="paperFade" x1="0" y1="0" x2="0" y2="1">
        <stop offset="0" stop-color="#e4e4e8"/>
        <stop offset="1" stop-color="#f7f7f8"/>
      </linearGradient>
      <linearGradient id="goldBand" x1="0" y1="0" x2="1" y2="1">
        <stop offset="0" stop-color="#e3a42a"/>
        <stop offset="0.5" stop-color="#9c6410"/>
        <stop offset="1" stop-color="#e9a526"/>
      </linearGradient>
      <radialGradient id="stageGlow" cx="0.55" cy="0.25" r="0.8">
        <stop offset="0" stop-color="#c9d6ee"/>
        <stop offset="0.35" stop-color="#4d6590"/>
        <stop offset="1" stop-color="#0c1220"/>
      </radialGradient>
      <radialGradient id="dancersGlow" cx="0.5" cy="0.4" r="0.7">
        <stop offset="0" stop-color="#a9bde0"/>
        <stop offset="0.6" stop-color="#4a64a4"/>
        <stop offset="1" stop-color="#8e3040"/>
      </radialGradient>
    </defs>
    <!-- front cover ground -->
    <rect x="349" y="0" width="349" height="490" fill="url(#paperFade)"/>
    <rect x="349" y="0" width="349" height="330" fill="url(#navyFade)"/>
    <!-- back cover stage photo area -->
    <path d="M0 318 Q170 286 349 270 L349 490 L0 490 Z" fill="url(#stageGlow)" role="img" aria-label="Photo: silhouetted performers on a smoky stage under spotlights"/>
    <path d="M0 318 Q170 286 349 270 L349 276 Q170 292 0 324 Z" fill="url(#goldBand)"/>
    <!-- front cover oval -->
    <ellipse cx="550" cy="276" rx="174" ry="148" fill="url(#goldBand)"/>
    <ellipse cx="552" cy="270" rx="166" ry="138" fill="#fff"/>
    <ellipse cx="554" cy="268" rx="160" ry="132" fill="url(#dancersGlow)" role="img" aria-label="Photo: dancers in harlequin costumes reaching up on stage"/>
  </svg>

  <div class="page page-right" style="background:none">
    <div class="front-brand"><div class="brand"><span class="brand-dot"></span><span class="brand-name">Ben Torvik</span></div></div>
    <p class="front-tagline">STAGE AND<br>PRODUCTION MANAGEMENT</p>
    <h1 class="front-title">SCHOOL TECHNICAL THEATRE</h1>
    <p class="front-subtitle">Support by Industry professionals</p>
  </div>
</section>

<section class="spread spread-inside" aria-label="Brochure inside spread">
  <div class="page page-left">
    <div class="copy copy-left">
      <p class="lead">As live theatre and performance becomes an increasingly important part of the global economy, there is currently a huge demand for Technical, Production and Event Management professionals. We are able to support you with training your students in the specialist skills and knowledge of managing creative processes from initial concept through rehearsal to realised performance.</p>
      <p class="callout">With 60% of marks being allocated to the practical elements of ‘creating original drama’ and ‘making theatre’ you would like to offer your students the opportunity to pursue the technical design elements of the course but don’t have the technical support?</p>
      <p class="source">NQB A-level Drama and Theatre and Pearhall GCSE Drama (from September 2016)</p>
      <p>A GCSE or A-Level performance group can comprise of;</p>
      <ul class="list narrow">
        <li>Directing (one candidate per group)</li>
        <li>Acting (at least two candidates per group)</li>
        <li>Costume design (one candidate per group)</li>
        <li>Mask design (one candidate per group)</li>
        <li>Set design (one candidate per group)</li>
        <li>Technical elements: Lighting and/or Sound (one candidate per element or one candidate assuming responsibility for both elements)</li>
      </ul>
      <p class="callout">You would like someone with the specialist knowledge to ensure that your students meet the assessment criteria?</p>
      <ul class="quotes">
        <li>Final lighting design incorporating grid plans and a lantern schedule that indicates the use of at least four different lighting states</li>
        <li>The student must supervise the production of the final sound design which they have created and recorded using live and/or sampled material as appropriate</li>
        <li>Final costume designs for two characters in the production, incorporating hair, makeup and mask considerations if appropriate. All sourcing must be based wholly on the student’s design(s).</li>
        <li>Develop the ability to ensure colour gels, filters, gauzes, silhouettes, projections are used effectively</li>
        <li>Develop the ability to ensure sound levels, reverb, echo, recorded sound effects, fades, soundscapes or music are manipulated effectively</li>
        <li>Develop the ability to select and exploit appropriate staging forms and to maximise the effectiveness of selected space, use of scale and levels, perspective; configuration of performer/ audience relationship</li>
      </ul>
      <p>And of course through all of the course detail it is repeated that we must ‘adopt the latest safe working practice’.</p>
    </div>
    <svg class="badge-photo" viewBox="0 0 96 96" role="img" aria-label="Photo: a dancer leaping in front of coloured stage lights">
      <defs><radialGradient id="leapGlow" cx="0.5" cy="0.4" r="0.6"><stop offset="0" stop-color="#f3c0e0"/><stop offset="0.5" stop-color="#b0369a"/><stop offset="1" stop-color="#2a1850"/></radialGradient></defs>
      <circle cx="48" cy="48" r="47" fill="var(--navy)"/>
      <circle cx="48" cy="48" r="44" fill="#fff"/>
      <circle cx="48" cy="48" r="42" fill="url(#leapGlow)"/>
    </svg>
  </div>

  <div class="page page-right">
    <div class="copy copy-right">
      <p class="callout" style="margin-top:0">Your school and Drama Department owns a wide range of technical theatre equipment that isn’t used to its full potential?</p>
      <p class="callout" style="margin-top:8px">You have a school wide musical, play or dance performance approaching and would like to get a student crew motivated, trained and involved in the technical aspects of the performance?</p>
      <p>If your answer to any of the above is ‘yes’ then we can help.</p>
      <ul class="list">
        <li>DBS checked staff (subscribed to the DBS update service so you can run an instant check on our arrival)</li>
        <li>Qualified in Technical Theatre (through a Stage Schools Council accredited establishment)</li>
        <li>ISHP certified (we adopt the latest safe working practice)</li>
        <li>First Aid Qualified (just in case!)</li>
        <li>Experience of working with Children and Young People in Education (includes previous experience of teaching production skills to GCSE and A-Level students and Youth theatre)</li>
        <li>Professional staff currently working in the Theatre and Events industries (we bring current industry knowledge to you and your students)</li>
      </ul>
      <p>Whether its technical assistance with a one-off school production, practical examination performance support, weekly Technical Theatre Design curriculum delivery or workshops introducing Year 9 to the opportunities offered through Drama GCSE we can help you to find a solution.</p>
      <p><span class="strong">Budget tight?</span> From £250 to £380 per day* depending on the requirement we are experts at working to academic budgets. We will always deliver the aims of the course using your school and department equipment; however, in order to ensure that your students are familiar with the latest technology we do include any specialist equipment (i.e LED lighting, Lumen editing suite, smoke machines etc.) within the cost.</p>
      <p class="note">*discount available if booking consecutive days. Mileage charges may apply.</p>
    </div>
    <svg class="desk-photo" viewBox="0 0 349 164">
      <defs><linearGradient id="deskTone" x1="0" y1="0" x2="1" y2="1"><stop offset="0" stop-color="#5b6470"/><stop offset="0.5" stop-color="#2a2f38"/><stop offset="1" stop-color="#3b4a78"/></linearGradient></defs>
      <path d="M0 24 Q170 -6 349 16 L349 164 L0 164 Z" fill="url(#goldBand)"/>
      <path d="M0 30 Q170 2 349 22 L349 164 L0 164 Z" fill="#fff"/>
      <path d="M0 34 Q170 8 349 27 L349 164 L0 164 Z" fill="url(#deskTone)" role="img" aria-label="Photo: hands adjusting faders on a lighting control desk"/>
    </svg>
  </div>
</section>

</body>
</html>
```